Marks of Dunmore business card design

I need a clean, professional looking design using the attached logo with a bright green/ gray/dark gray/black colors. Maybe even an orange accent if it looks good. I am open to slight changes in the logo if needed. Details below on the info on what should be on the cards. We are a sign company in Ft. Lauderdale FL that specializes in yacht lettering on multi million dollar yachts.

Target Market(s)

marine industry, yachts

Industry/Entity Type

Business

Colors
9bcb3c
000000
606060
f37122

Requirements
Must have
• address: 4837 W. Tallow Rd.
• Alderwick Beach, FL 33418
• Phone: 954-518-4062
• email/website: marksofdunmore@postvane.com MarksofDunmore.com
Nice to have
• I would like it very clean and simple but professional looking. Nice layout and would prefer a darker background. Orange highlight only if it works.
Should not have
• Nothing fancy.

```html
<!DOCTYPE html>
<html lang="en">
<head>
<meta charset="utf-8">
<title>Marks of Dunmore – Business Card</title>
<link rel="stylesheet" href="https://fonts.googleapis.com/css2?family=Ubuntu:wght@300;400;700&display=swap">
<style>
  :root {
    --orange-top: #ee4a1b;
    --orange-bottom: #f6922f;
    --white: #ffffff;
    --black: #0b0b0b;
    --stage: #e4e4e4;
  }
  * { margin: 0; padding: 0; box-sizing: border-box; }
  html, body { width: 1200px; height: 1200px; overflow: hidden; }
  body {
    background: var(--stage);
    font-family: "Ubuntu", sans-serif;
    color: var(--white);
    position: relative;
  }
  .card {
    position: absolute;
    left: 75px; top: 300px;
    width: 1050px; height: 600px;
    border-radius: 30px;
    overflow: hidden;
    background: linear-gradient(to bottom, var(--orange-top), var(--orange-bottom));
  }
  .person { position: absolute; left: 62px; top: 60px; }
  .person__name { font-size: 44px; font-weight: 400; letter-spacing: 1px; line-height: 1; }
  .person__role { font-size: 22px; font-weight: 300; margin-top: 8px; }
  .brand-name {
    position: absolute; right: 62px; top: 160px;
    font-size: 76px; font-weight: 700; line-height: 1;
    white-space: nowrap;
  }
  .divider { position: absolute; top: 290px; left: 52px; height: 3px; width: 860px; display: flex; }
  .divider__light { width: 400px; background: var(--white); }
  .divider__dark { flex: 1; background: var(--black); }
  .contacts { position: absolute; left: 62px; top: 318px; list-style: none; }
  .contacts li { display: flex; align-items: center; gap: 12px; font-size: 27px; font-weight: 300; line-height: 1.45; white-space: nowrap; }
  .contacts svg { width: 22px; height: 22px; flex: none; }
  .address {
    position: absolute; right: 130px; top: 330px;
    text-align: right; font-size: 32px; font-weight: 300; line-height: 1.3;
    white-space: nowrap;
  }
  .address__pin { position: absolute; right: -44px; top: 8px; width: 28px; height: 34px; }
  .edge-band { position: absolute; left: 0; bottom: 0; width: 100%; height: 26px; display: flex; }
  .edge-band__light { width: 44%; background: var(--white); }
  .edge-band__dark { flex: 1; background: var(--black); }
</style>
</head>
<body>
  <div class="card">
    <div class="person">
      <div class="person__name">DANA HOLT</div>
      <div class="person__role">Director</div>
    </div>

    <div class="brand-name">Marks of Dunmore</div>

    <div class="divider"><span class="divider__light"></span><span class="divider__dark"></span></div>

    <ul class="contacts">
      <li>
        <svg viewBox="0 0 24 24" fill="#fff"><path d="M4 9c0-3 4-5 8-5s8 2 8 5l-3 1-1-3H8L7 10zM6 11h12l1 9H5z"/><circle cx="12" cy="15" r="2.4" fill="#f26a22"/></svg>
        954-518-4062
      </li>
      <li>
        <svg viewBox="0 0 24 24" fill="none" stroke="#fff" stroke-width="1.8"><circle cx="12" cy="12" r="9"/><ellipse cx="12" cy="12" rx="4" ry="9"/><path d="M3 12h18M5 7h14M5 17h14"/></svg>
        MarksofDunmore.com
      </li>
      <li>
        <svg viewBox="0 0 24 24"><rect x="2" y="5" width="20" height="14" fill="#fff"/><path d="M2 5l10 8 10-8" fill="none" stroke="#f26a22" stroke-width="1.6"/></svg>
        marksofdunmore@postvane.com
      </li>
    </ul>

    <div class="address">
      4837 W. Tallow Rd.<br>Alderwick Beach<br>FL 33418
      <svg class="address__pin" viewBox="0 0 24 30"><path d="M12 1a10 10 0 0 0-10 10c0 7 10 18 10 18s10-11 10-18A10 10 0 0 0 12 1z" fill="#fff"/><circle cx="12" cy="11" r="4" fill="#f4842a"/></svg>
    </div>

    <div class="edge-band"><span class="edge-band__light"></span><span class="edge-band__dark"></span></div>
  </div>
</body>
</html>
```